Company Capability Brochure

Want to create a mulit paged brochure to hand out to potential clients to show our services and capabilities.

Attached is a rough draft we made using chatgpt which can be use as an example and includes the categories, text, our logo and preferred colour scheme we wish to use.
Would like to make this more look more visually appealing and a more professional layout over more pages.

```html
<!DOCTYPE html>
<html lang="en">
<head>
<meta charset="utf-8">
<title>Clearpoint Security Services – Capability Brochure</title>
<link rel="stylesheet" href="https://fonts.googleapis.com/css2?family=Audiowide&family=Michroma&family=Poppins:wght@400;500;600&display=swap">
<style>
:root{
  --stage:#e4e4e4;
  --navy:#050d24;
  --navy-mid:#0a1f4d;
  --blue:#1a6fd6;
  --cyan:#27b6f0;
  --bright:#3fd0ff;
  --white:#ffffff;
  --ink:#0b1a3a;
  --grey:#c9d3e4;
}
*{margin:0;padding:0;box-sizing:border-box}
html,body{width:955px;height:1200px;overflow:hidden;background:var(--stage)}
body{position:relative;font-family:"Poppins",sans-serif}
.page{position:absolute;width:358px;height:462px;overflow:hidden;box-shadow:6px 10px 22px rgba(0,0,0,.28)}
.page--cover{left:99px;top:117px;background:radial-gradient(ellipse at 70% 70%,#1c5fc4 0%,#0b2a6b 40%,var(--navy) 80%)}
.page--back{left:498px;top:117px;background:radial-gradient(ellipse at 50% 0%,#1c58c8 0%,#0a1f55 35%,var(--navy) 70%),var(--navy)}
.page--about{left:99px;top:622px;background:linear-gradient(160deg,#07112b 0%,var(--navy) 55%,#0c2a68 100%)}
.page--services{left:498px;top:622px;background:var(--white)}
.abs{position:absolute}
.brand{display:flex;align-items:center;gap:6px;justify-content:center;left:0;right:0}
.brand__dot{width:14px;height:14px;border-radius:50%;background:var(--cyan)}
.brand__name{font-family:"Michroma",sans-serif;font-size:9.5px;letter-spacing:1.6px;color:var(--cyan)}
.cover__kicker{left:0;right:0;top:84px;text-align:center;color:var(--white);font-family:"Michroma",sans-serif;font-size:9.5px;letter-spacing:4px}
.cover__make{left:0;right:0;top:96px;text-align:center;color:var(--white);font-family:"Audiowide",sans-serif;font-size:21px}
.cover__big{left:0;right:0;text-align:center;font-family:"Audiowide",sans-serif;font-size:47px;line-height:1;background:linear-gradient(180deg,#4fd2ff,#1a6fd6);-webkit-background-clip:text;background-clip:text;color:transparent}
.photo{position:absolute;border-radius:3px}
.pill{display:flex;left:50%;transform:translateX(-50%);border-radius:10px;overflow:hidden;font-weight:600;color:var(--white);white-space:nowrap}
.pill span:first-child{background:linear-gradient(90deg,#1e82e0,#29b1f0);padding:3px 8px;letter-spacing:.7px}
.pill span:last-child{background:#0f2f8a;padding:3px 8px}
.web{left:0;right:0;text-align:center;color:var(--white);font-size:7px;letter-spacing:1.8px}
.web b{color:var(--cyan);font-weight:500}
.clients__title{left:30px;right:30px;top:169px;display:flex;align-items:center;gap:6px;font-family:"Audiowide",sans-serif;font-size:11px;color:var(--cyan)}
.clients__title::before,.clients__title::after{content:"";flex:1;height:1px;background:#6f86b8}
.clients__title::before{flex:1.6}
.clients{left:29px;top:187px;display:grid;grid-template-columns:repeat(5,57px);grid-auto-rows:24px;gap:3px}
.clients__cell{background:var(--white);border-radius:2px;display:flex;align-items:center;justify-content:center;font-size:6.3px;font-weight:600;color:var(--ink);letter-spacing:.3px}
.contact__icons{left:0;right:0;top:298px;display:flex;justify-content:center;gap:5px}
.contact__icon{width:11px;height:11px;border-radius:50%;background:var(--blue);display:flex;align-items:center;justify-content:center}
.contact__line{left:0;right:0;text-align:center;color:var(--white);font-size:8px;font-weight:500}
.back__tag{left:0;right:0;top:367px;text-align:center;font-family:"Audiowide",sans-serif;font-size:11px;line-height:11.5px;color:var(--cyan)}
.about__word{left:268px;top:0;width:462px;height:92px;transform-origin:0 0;transform:translate(92px,0) rotate(90deg);font-family:"Audiowide",sans-serif;font-size:104px;line-height:92px;letter-spacing:2px;background:linear-gradient(90deg,#1a6fd6,#27b6f0 60%,#1250b0);-webkit-background-clip:text;background-clip:text;color:transparent;white-space:nowrap}
.statement__head{left:28px;font-family:"Audiowide",sans-serif;font-size:11px;line-height:11px;color:var(--white)}
.statement__head em{font-style:normal;color:var(--cyan);display:block}
.statement__body{left:28px;width:170px;border-left:1px solid #56698f;padding-left:5px;color:var(--grey);font-size:4.3px;line-height:5.9px;text-align:justify}
.folio{left:28px;right:28px;top:424px;display:flex;align-items:center;gap:5px;font-size:5px;letter-spacing:.4px}
.folio::after{content:"";flex:1;height:1px;background:#5d6f94}
.folio__num{position:absolute;right:-6px;top:-3px;width:11px;height:11px;border-radius:50%;background:#0f2f8a;color:var(--white);font-size:5px;display:flex;align-items:center;justify-content:center;border:1px solid var(--cyan)}
.services__title{left:77px;top:42px;font-family:"Audiowide",sans-serif;font-size:14px;line-height:14px;color:var(--ink)}
.services__band{left:28px;top:84px;width:30px;height:227px;border-radius:0 0 0 6px;background:linear-gradient(180deg,#27b6f0,#1a6fd6)}
.services__panel{left:55px;top:80px;width:273px;height:231px;border-radius:6px;background:linear-gradient(120deg,#1a6fd6 0%,#0c2f78 45%,var(--navy) 100%)}
.service{left:44px;width:284px;height:36px}
.service__icon{position:absolute;left:0;top:2px;width:25px;height:25px;border-radius:4px;background:#0b2a6b;border:1px solid #5aa8ff;display:flex;align-items:center;justify-content:center}
.service__name{position:absolute;left:32px;top:0;font-family:"Michroma",sans-serif;font-size:6.5px;color:var(--bright)}
.service__text{position:absolute;left:32px;top:10px;width:232px;font-size:4.3px;line-height:5.8px;color:var(--white)}
.service__rule{position:absolute;left:32px;right:12px;bottom:-2px;height:1px;background:rgba(255,255,255,.25)}
.gallery{left:28px;top:324px;display:flex;gap:4px}
.gallery__photo{width:57px;height:70px;border-radius:3px;border:1px solid #7aa3d8}
</style>
</head>
<body>

<!-- Cover -->
<section class="page page--cover">
  <div class="abs brand" style="top:28px"><span class="brand__dot"></span><span class="brand__name">CLEARPOINT SECURITY</span></div>
  <div class="abs cover__kicker">BE INFORMED AND</div>
  <div class="abs cover__make">MAKE THE</div>
  <div class="abs cover__big" style="top:116px">RIGHT</div>
  <div class="abs cover__big" style="top:160px">CHOICE</div>
  <div class="photo" role="img" aria-label="Security cameras, alarm keypad and shield emblem product arrangement" style="left:55px;top:200px;width:250px;height:188px;background:radial-gradient(ellipse at 55% 45%,#b9c7d8 0%,#5a7aa8 35%,rgba(16,60,140,.5) 70%,transparent 85%)"></div>
  <div class="abs pill" style="top:396px;font-size:7.5px"><span>MASTER LICENSE</span><span>40912345</span></div>
  <div class="abs web" style="top:426px">www.<b>clearpointsecurity</b>.com.au</div>
</section>

<!-- Back cover -->
<section class="page page--back">
  <div class="photo" role="img" aria-label="White dome security camera with shield emblem" style="left:110px;top:25px;width:140px;height:125px;background:radial-gradient(ellipse at 45% 45%,#f2f4f7 0%,#aab4c4 40%,#2c4a80 70%,transparent 85%)"></div>
  <div class="abs clients__title">OUR CLIENTS</div>
  <div class="abs clients">
    <div class="clients__cell">HARBOURLINE</div>
    <div class="clients__cell">Westmere</div>
    <div class="clients__cell">ARDENT COLLEGE</div>
    <div class="clients__cell">Lumen Group</div>
    <div class="clients__cell">Fairlane</div>
    <div class="clients__cell">Keystone</div>
    <div class="clients__cell">Nordal Strata</div>
    <div class="clients__cell">Bayview</div>
    <div class="clients__cell">Redgum Club</div>
    <div class="clients__cell">HOLLOWAY</div>
  </div>
  <div class="abs brand" style="top:258px"><span class="brand__dot"></span><span class="brand__name">CLEARPOINT SECURITY</span></div>
  <div class="abs contact__icons">
    <span class="contact__icon"><svg width="6" height="6" viewBox="0 0 10 10"><path d="M2 1l2 2-1 1.2a6 6 0 0 0 2.8 2.8L7 6l2 2-1.3 1.3C4.5 9 1 5.5.7 2.3z" fill="#fff"/></svg></span>
    <span class="contact__icon"><svg width="6" height="6" viewBox="0 0 10 10"><rect x="1" y="2" width="8" height="6" fill="#fff"/><path d="M1 2l4 3 4-3" stroke="#1a6fd6" fill="none"/></svg></span>
    <span class="contact__icon"><svg width="6" height="6" viewBox="0 0 10 10"><path d="M5 9S1.5 5.5 1.5 3.5a3.5 3.5 0 0 1 7 0C8.5 5.5 5 9 5 9z" fill="#fff"/></svg></span>
  </div>
  <div class="abs contact__line" style="top:313px">1300 555 018</div>
  <div class="abs contact__line" style="top:329px">info@clearpointsecurity.com.au</div>
  <div class="abs contact__line" style="top:345px">12/8 Harlow St, Riverton, NSW 2150</div>
  <div class="abs back__tag">BE INFORMED AND MAKE<br>THE RIGHT CHOICE</div>
  <div class="abs pill" style="top:400px;font-size:6.5px"><span>MASTER LICENSE</span><span>40912345</span></div>
  <div class="abs web" style="top:424px">www.<b>clearpointsecurity</b>.com.au</div>
</section>

<!-- About us -->
<section class="page page--about">
  <div class="abs about__word">ABOUT US</div>
  <div class="photo" role="img" aria-label="Silver bullet security camera on wall mount" style="left:215px;top:290px;width:143px;height:172px;background:radial-gradient(ellipse at 55% 40%,#e3e8ee 0%,#9aa8bb 40%,rgba(20,50,110,.4) 75%,transparent 90%)"></div>

  <div class="abs statement__head" style="top:28px"><em>Mission</em>Statement</div>
  <p class="abs statement__body" style="top:58px">Our mission is to deliver exceptional service and cutting-edge Electronic and Mechanical Security Solutions that not only meet but consistently exceed our clients' expectations. We are dedicated to ensuring the safety, protection, and peace of mind of those we serve by combining advanced technologies, industry expertise, and a relentless focus on quality, reliability, and customer satisfaction. Through personalized solutions, responsive support, and continuous innovation, we aim to build long-term partnerships and be a trusted name in security.</p>

  <div class="abs statement__head" style="top:139px"><em>Vision</em>Statement</div>
  <p class="abs statement__body" style="top:169px">Our vision is to be the most trusted, innovative, and customer-focused partner in the security industry, renowned for the professional installation, service, and maintenance of Electronic and Mechanical Security Systems. We strive to set the benchmark for excellence by delivering tailored, reliable, and future-ready solutions that protect what matters most to our clients, while building lasting relationships based on integrity, responsiveness, and continuous improvement.</p>

  <div class="abs statement__head" style="top:238px"><em>Culture</em>Statement</div>
  <p class="abs statement__body" style="top:268px">At the heart of our company is a culture driven by trust, innovation, and service excellence. We are a team of dedicated professionals who take pride in protecting what matters most to our clients through advanced Electronic and Mechanical Security Solutions.</p>
  <p class="abs statement__body" style="top:306px">We cultivate a work environment built on integrity, mutual respect, and accountability, where every team member is empowered to grow, contribute ideas, and take ownership of outcomes. Collaboration, continuous improvement, and a commitment to exceeding expectations define how we operate—both with our clients and each other.</p>
  <p class="abs statement__body" style="top:355px">We embrace change, champion innovation, and remain agile in an evolving industry—always striving to deliver smarter, more reliable, and more secure solutions. Together, we are building not just systems, but lasting partnerships and a safer future.</p>

  <div class="abs folio" style="color:var(--white)"><span>www.<b style="color:var(--cyan);font-weight:500">clearpointsecurity</b>.com.au</span><span class="folio__num">1</span></div>
</section>

<!-- Our services -->
<section class="page page--services">
  <div class="photo" role="img" aria-label="Metal shield emblem with fingerprint" style="left:20px;top:27px;width:45px;height:55px;background:linear-gradient(160deg,#d7dbe0,#5b6270);border-radius:4px 4px 22px 22px"></div>
  <div class="abs services__title">Our<br>Services</div>
  <div class="abs services__band"></div>
  <div class="abs services__panel"></div>

  <div class="abs service" style="top:97px">
    <span class="service__icon"><svg width="11" height="11" viewBox="0 0 12 12"><rect x="1" y="2" width="10" height="2" fill="#fff"/><circle cx="6" cy="7.5" r="3" fill="#fff"/><circle cx="6" cy="7.5" r="1.2" fill="#0b2a6b"/></svg></span>
    <span class="service__name">CCTV Systems</span>
    <p class="service__text">Lorem ipsum dolor sit amet, consectetur adipiscing elit, sed do eiusmod tempor incididunt ut labore et dolore magna aliqua. Quis ipsum suspendisse ultrices gravida. Risus commodo.</p>
    <span class="service__rule"></span>
  </div>
  <div class="abs service" style="top:140px">
    <span class="service__icon"><svg width="11" height="11" viewBox="0 0 12 12"><rect x="3" y="1" width="6" height="10" rx="1" fill="none" stroke="#fff"/><circle cx="6" cy="4" r="1" fill="#fff"/><rect x="4.5" y="6.5" width="3" height="2" fill="#fff"/></svg></span>
    <span class="service__name">Access Control</span>
    <p class="service__text">Lorem ipsum dolor sit amet, consectetur adipiscing elit, sed do eiusmod tempor incididunt ut labore et dolore magna aliqua. Quis ipsum suspendisse ultrices gravida. Risus commodo.</p>
    <span class="service__rule"></span>
  </div>
  <div class="abs service" style="top:183px">
    <span class="service__icon"><svg width="11" height="11" viewBox="0 0 12 12"><rect x="3" y="1" width="6" height="10" rx="1" fill="none" stroke="#fff"/><circle cx="6" cy="4" r="1.3" fill="#fff"/><path d="M4.5 7h3M4.5 8.5h3" stroke="#fff" stroke-width=".7"/></svg></span>
    <span class="service__name">Intercoms</span>
    <p class="service__text">Lorem ipsum dolor sit amet, consectetur adipiscing elit, sed do eiusmod tempor incididunt ut labore et dolore magna aliqua. Quis ipsum suspendisse ultrices gravida. Risus commodo.</p>
    <span class="service__rule"></span>
  </div>
  <div class="abs service" style="top:227px">
    <span class="service__icon"><svg width="11" height="11" viewBox="0 0 12 12"><path d="M6 1.5a3 3 0 0 1 3 3V8l1 1.5H2L3 8V4.5a3 3 0 0 1 3-3z" fill="#fff"/><circle cx="6" cy="10.5" r="1" fill="#fff"/></svg></span>
    <span class="service__name">Alarms</span>
    <p class="service__text">Lorem ipsum dolor sit amet, consectetur adipiscing elit, sed do eiusmod tempor incididunt ut labore et dolore magna aliqua. Quis ipsum suspendisse ultrices gravida. Risus commodo.</p>
    <span class="service__rule"></span>
  </div>
  <div class="abs service" style="top:273px">
    <span class="service__icon"><svg width="11" height="11" viewBox="0 0 12 12"><path d="M1 1v10M11 1v10" stroke="#fff" stroke-width="1.4"/><path d="M2.5 2.5L5.5 4v4l-3 1.5zM9.5 2.5L6.5 4v4l3 1.5z" fill="#fff"/></svg></span>
    <span class="service__name">Gates</span>
    <p class="service__text">Lorem ipsum dolor sit amet, consectetur adipiscing elit, sed do eiusmod tempor incididunt ut labore et dolore magna aliqua. Quis ipsum suspendisse ultrices gravida. Risus commodo.</p>
  </div>

  <div class="abs gallery">
    <div class="gallery__photo" role="img" aria-label="CCTV cameras on a pole against blue sky" style="background:linear-gradient(180deg,#4f8fd0,#b8d3ee)"></div>
    <div class="gallery__photo" role="img" aria-label="Access control keypad beside a glass door handle" style="background:linear-gradient(90deg,#8a8f96,#3a3f46)"></div>
    <div class="gallery__photo" role="img" aria-label="Wall of intercom panels in red and grey" style="background:linear-gradient(180deg,#c4353f,#6a6f7a)"></div>
    <div class="gallery__photo" role="img" aria-label="Alarm panel controlled from a smartphone" style="background:linear-gradient(180deg,#eceff2,#b9bec6)"></div>
    <div class="gallery__photo" role="img" aria-label="Technician working at security gate equipment" style="background:linear-gradient(90deg,#1b2e52,#4a6ea3)"></div>
  </div>

  <div class="abs folio" style="color:var(--ink)"><span>www.<b style="color:var(--blue);font-weight:500">clearpointsecurity</b>.com.au</span><span class="folio__num">2</span></div>
</section>

</body>
</html>
```